Webshop for baby shoes need new design

We are an innovative company selling a one of a kind product on a market with tough competition. We are looking to step up our business and need a new design for our shop.

We are looking for recognition as well as originality. The customer must immediately be able to identify navigation, shopping cart, buy buttons etc. We want warm welcoming colors, but not too strong as to not draw attention away from the products. Retro might be interesting, if "done right".

Suggested color palette: http://huepalettemaker.example/#7k29WbQx3p8r5

We have a logo (attached), but if you have a better idea we might go for that instead. Also, a couple of product images are attached for you to use in the design.

What we do NOT want is a shop that looks like a free template (vendaForge etc). Also, while we are selling baby shoes, we don't want to use the very worn our baby pink/blue scheme, so stay clear of this, thanks.
Updates

We suggest that you use this palette, or similar: http://huepalettemaker.example/#7k29WbQx3p8r5

Project Deadline Extended
Reason: We feel that we are getting closer to finding a design that we like, but there is still a bit to go. Also we want to give the chance to any late starters to show their idea. The competition is still open.

Target Market(s)

babies and their parents

Industry/Entity Type

Shopping

Requirements
Must have
• The usual webshop elements
- shopping cart
- product listing
- product page
- buy buttons
Nice to have
• - large footer area for links, info and function (see trindel.example for an example)
- some kind of product navigation/filter (left, top or right)
- place for promotion banners

```html
<!DOCTYPE html>
<html lang="en">
<head>
<meta charset="utf-8">
<title>Toddlek – Children's Fitted Footwear</title>
<link rel="stylesheet" href="https://fonts.googleapis.com/css2?family=Noto+Serif:wght@400;700&family=Arimo:wght@400;700&family=Parisienne&display=swap">
<style>
:root{
  --cream:#efebe3;
  --brown-deep:#4a280f;
  --brown-dark:#5b3316;
  --brown:#6e3f1c;
  --tan:#a8703d;
  --tan-light:#c99a63;
  --sand:#d7bd93;
  --ink:#3a2515;
  --muted:#7b6a5a;
  --red:#b3141a;
  --white:#ffffff;
  --card:#f7f6f4;
  --serif:'Noto Serif', Georgia, serif;
  --sans:'Arimo', Arial, sans-serif;
}
*{box-sizing:border-box;margin:0;padding:0}
html,body{width:991px;height:1200px;overflow:hidden}
body{background:var(--cream);font-family:var(--sans);color:var(--ink);position:relative}
a{color:inherit}
.abs{position:absolute}

/* header */
.brand{left:124px;top:14px;display:flex;align-items:center;gap:12px}
.brand-mark{width:60px;height:60px;border-radius:8px;background:var(--tan)}
.brand-name{font-family:var(--serif);font-weight:700;font-size:46px;color:var(--tan);letter-spacing:1px}
.basket{left:601px;top:14px;width:281px;height:63px;background:#fbfaf8;border:1px solid #e2dbd0;border-radius:8px;padding:4px 12px}
.basket h2{font-family:var(--sans);font-weight:700;font-size:18px;color:#9a6a3a}
.basket .count{font-size:9px;color:var(--muted);margin-top:3px}
.basket .total{font-size:9px;font-weight:700;color:#5a4535;margin-top:3px}
.basket .account{position:absolute;right:18px;top:8px;font-size:9px;font-weight:700;color:#5a4535}
.basket .view{position:absolute;right:18px;top:44px;font-size:9px;color:#8a6a4a;display:flex;align-items:center;gap:5px}

/* navigation */
.nav{left:109px;top:93px;width:773px;height:53px;border-radius:8px;background:linear-gradient(#a86f3b,#8a5426);border:2px dashed #d9a56c;outline:2px solid #8a5426;display:flex;align-items:center;padding-left:9px}
.nav a{font-family:var(--serif);font-weight:700;font-size:16px;color:#f6ecdc;text-decoration:none;margin-right:24px}
.nav a.current{background:#5e3214;height:41px;width:93px;display:flex;align-items:center;justify-content:center;margin-right:25px;border-radius:3px}
.search{position:absolute;left:590px;top:12px;width:165px;height:23px;border-radius:4px;background:#c8a070}
.search .go{position:absolute;right:3px;top:3px;width:17px;height:17px;border-radius:4px;background:#e9dcc8;display:flex;align-items:center;justify-content:center}

/* hero */
.hero{left:107px;top:153px;width:775px;height:259px;border-radius:8px;background:radial-gradient(ellipse at 40% 50%,#a56e42,#6b3c1c);border:2px solid #8a5426;overflow:hidden}
.hero-photo{position:absolute;right:10px;top:0;width:470px;height:257px;background:radial-gradient(ellipse at 60% 55%,#2f4c7c 0%,#3b5a8a 30%,rgba(130,85,50,0) 70%)}
.hero h1{position:absolute;font-family:var(--serif);font-weight:700;color:#f3e6d2}
.hero .l1{left:30px;top:18px;font-size:37px}
.hero .l2{left:73px;top:62px;font-size:37px}
.hero .l3{left:30px;top:105px;font-size:54px;color:#fbe9d6}
.hero .tag{position:absolute;left:30px;top:172px;font-family:var(--serif);font-weight:700;font-size:16px;color:#fff}
.hero .cta{position:absolute;left:28px;top:215px;width:175px;height:24px;border-radius:3px;background:var(--red);color:#fff;font-family:var(--serif);font-weight:700;font-size:12px;display:flex;align-items:center;padding-left:13px;gap:10px}
.arrow-dot{width:16px;height:16px;border-radius:50%;background:#fff;display:inline-flex;align-items:center;justify-content:center}

/* filter sidebar */
.filters{left:107px;top:429px;width:163px;height:519px;background:var(--brown-dark);border:2px solid #8a5426;border-radius:5px;color:#fff;padding:12px 0 0 18px}
.filters h3{font-size:10px;font-weight:700;margin-left:3px}
.filters .grp{position:absolute;left:18px;width:118px;border-top:1px dotted #b08a64;padding-top:7px;font-size:9px}
.filters .grp b{display:block;font-weight:700;margin-bottom:4px}
.filters .grp a{display:block;line-height:11.6px;text-decoration:underline}
.filters select{width:94px;height:15px;font-size:9px;color:#777;border:1px solid #999;background:#fff}
.side-toggle{left:272px;top:434px;width:17px;height:17px;border-radius:50%;background:#e7e1d8;display:flex;align-items:center;justify-content:center}

/* promos */
.promo{top:428px;width:187px;height:167px;border-radius:5px;background:#8b5a2f;overflow:hidden}
.promo .head{height:28px;background:var(--brown-dark);display:flex;align-items:center;justify-content:space-between;padding:0 8px 0 18px;font-family:var(--serif);font-weight:700;font-size:16px;color:#fff}
.promo .photo{margin:2px 3px;height:132px;border:2px solid #f2ece5}
.rating{left:696px;top:428px;width:187px;height:167px;border-radius:5px;background:radial-gradient(#b0703f,#7a4320);border:2px dashed #d69d66;overflow:hidden}
.rating p{position:absolute;left:18px;top:10px;width:130px;font-family:'Parisienne',cursive;font-size:20px;line-height:23px;color:#fff}
.rating .pct{position:absolute;left:121px;top:2px;width:60px;height:60px;border-radius:50%;background:#5a3016;color:#fff;font-family:var(--serif);font-weight:700;font-size:22px;display:flex;align-items:center;justify-content:center}
.rating .btn{position:absolute;left:35px;top:136px;width:121px;height:18px;border-radius:3px;background:var(--red);color:#fff;font-family:var(--serif);font-weight:700;font-size:9px;display:flex;align-items:center;justify-content:center}

/* collection */
.section-title{left:311px;top:607px;font-family:var(--serif);font-weight:700;font-size:16px;color:#6b3c1c}
.card{width:142px;height:147px;background:linear-gradient(#fff,#f1f0ee);border:1px solid #e5e2dd;border-radius:3px}
.card .photo{position:absolute;left:14px;top:5px;width:114px;height:70px;border-radius:6px}
.card .name{position:absolute;left:12px;top:85px;font-size:12px;color:#4a3525}
.card .type{position:absolute;left:12px;top:99px;font-size:9px;color:var(--muted)}
.card .price{position:absolute;right:12px;top:85px;font-size:12px;color:#3a2515}
.card .add{position:absolute;left:30px;top:124px;width:86px;height:17px;border-radius:9px;background:var(--brown-dark);color:#fff;font-size:9px;display:flex;align-items:center;padding-left:8px;gap:11px}
.card .add .plus{width:15px;height:15px;border-radius:50%;background:#fff;color:var(--brown-dark);font-weight:700;font-size:12px;display:flex;align-items:center;justify-content:center}
.shoe-blue{background:radial-gradient(ellipse at 50% 55%,#2f4a7e 0%,#5f80ae 35%,#f5f5f5 72%)}
.shoe-orange{background:radial-gradient(ellipse at 50% 55%,#2f4a7e 0%,#d2773c 30%,#f5f5f5 72%)}
.shoe-white{background:radial-gradient(ellipse at 50% 55%,#e9e3cf 0%,#f2eee2 40%,#f8f8f8 72%)}
.shoe-teal{background:radial-gradient(ellipse at 50% 55%,#22536a 0%,#3d7388 35%,#f5f5f5 72%)}

/* footer */
.footer{left:0;top:987px;width:991px;height:164px;background:var(--brown-dark);border-top:3px solid #b7865a}
.footer .col{position:absolute;top:24px}
.footer h4{font-family:var(--serif);font-weight:700;font-size:11.5px;color:#f3e6d4;margin-bottom:6px}
.footer li{list-style:none;font-size:9.5px;line-height:17.8px;color:#eadbc6;letter-spacing:.3px}
.footer-brand{position:absolute;left:640px;top:21px;display:flex;align-items:center;gap:10px}
.footer-brand .brand-name{font-size:40px;color:var(--tan-light)}
.footer-brand .brand-mark{width:56px;height:56px;background:var(--tan-light)}
.social{position:absolute;left:793px;top:138px;display:flex;gap:5px}
.social span{width:15px;height:15px;border-radius:3px;background:#d9cbb7}
.legal{left:0;top:1151px;width:991px;height:49px;background:var(--brown);border-top:1px solid #8a5a33;font-size:9.5px;color:#f1e4d2;padding:17px 0 0 109px}
</style>
</head>
<body>

<header>
  <div class="brand abs">
    <span class="brand-mark"></span>
    <span class="brand-name">Toddlek</span>
  </div>
  <div class="basket abs">
    <h2>Your Basket</h2>
    <p class="count">0 items</p>
    <p class="total">total: 0.00</p>
    <span class="account">Register / Log in</span>
    <span class="view">
      <svg width="13" height="13" viewBox="0 0 13 13"><path d="M1 5h11l-1.5 7h-8z" fill="#c9a878"/><path d="M4 5l2.5-4 2.5 4" fill="none" stroke="#8a6a4a" stroke-width="1.2"/></svg>
      view basket
    </span>
  </div>
</header>

<nav class="nav abs">
  <a class="current" href="#">Home</a>
  <a href="#">Girls</a>
  <a href="#">Boys</a>
  <a href="#">Store Locator</a>
  <a href="#">Fitting</a>
  <a href="#">About Us</a>
  <div class="search">
    <span class="go"><svg width="10" height="10" viewBox="0 0 10 10"><circle cx="4" cy="4" r="3" fill="none" stroke="#6b4a2a" stroke-width="1.4"/><path d="M6.3 6.3l2.7 2.7" stroke="#6b4a2a" stroke-width="1.6"/></svg></span>
  </div>
</nav>

<section class="hero abs">
  <div class="hero-photo" role="img" aria-label="Two children's leather shoes in navy, teal and orange with white soles"></div>
  <h1 class="l1">Quality &amp;</h1>
  <h1 class="l2">Durability</h1>
  <h1 class="l3">Fit &amp; Style</h1>
  <p class="tag">Experts in Childrens fitted footwear</p>
  <a class="cta" href="#">SEE OUR COLECTION <span class="arrow-dot"><svg width="8" height="8" viewBox="0 0 8 8"><path d="M2.5 1l3 3-3 3" fill="none" stroke="#b3141a" stroke-width="1.6"/></svg></span></a>
</section>

<aside class="filters abs">
  <h3>narrow by:</h3>
  <div class="grp" style="top:36px">
    <b>special offers</b><a href="#">Sale only</a>
  </div>
  <div class="grp" style="top:76px">
    <b>category</b>
    <a href="#">Boots</a><a href="#">Canvas</a><a href="#">English Classics</a><a href="#">First Walking Shoes</a><a href="#">Non-school Shoes</a><a href="#">Pre-walkers</a><a href="#">Sandals</a><a href="#">School Shoes</a><a href="#">Trainers</a><a href="#">Wellies</a>
  </div>
  <div class="grp" style="top:222px">
    <b>gender</b><a href="#">Boys</a><a href="#">Boys &amp; Girls</a>
  </div>
  <div class="grp" style="top:274px">
    <b>sizes</b><select><option>Please select</option></select>
  </div>
  <div class="grp" style="top:317px">
    <b>fit</b><select><option>Please select</option></select>
  </div>
  <div class="grp" style="top:359px">
    <b>colour</b><select><option>Please select</option></select>
  </div>
  <div class="grp" style="top:401px">
    <b>styling</b>
    <a href="#">Closed Shoe</a><a href="#">Buckle</a><a href="#">Laces</a><a href="#">Riptape</a><a href="#">Slip-on</a><a href="#">T-bars</a><a href="#">Zip</a>
  </div>
</aside>
<span class="side-toggle abs"><svg width="7" height="8" viewBox="0 0 7 8"><path d="M2 1l3 3-3 3" fill="none" stroke="#fff" stroke-width="1.5"/></svg></span>

<section class="promo abs" style="left:304px">
  <div class="head">New Arrivals <span class="arrow-dot"><svg width="8" height="8" viewBox="0 0 8 8"><path d="M2.5 1l3 3-3 3" fill="none" stroke="#5b3316" stroke-width="1.6"/></svg></span></div>
  <div class="photo shoe-blue" role="img" aria-label="Navy and light blue laced baby shoe"></div>
</section>
<section class="promo abs" style="left:500px">
  <div class="head">Special Offers <span class="arrow-dot"><svg width="8" height="8" viewBox="0 0 8 8"><path d="M2.5 1l3 3-3 3" fill="none" stroke="#5b3316" stroke-width="1.6"/></svg></span></div>
  <div class="photo" style="background:linear-gradient(135deg,#d9a86a,#c98f52 50%,#e0b887)" role="img" aria-label="Red and white baby sneakers beside a wooden toy on a wooden floor"></div>
</section>
<section class="rating abs">
  <p>Our Customers rate our excellent service</p>
  <span class="pct">95%</span>
  <a class="btn" href="#">STORE LOCATOR</a>
</section>

<h2 class="section-title abs">Winter Collection</h2>

<main>
  <article class="card abs" style="left:304px;top:639px"><div class="photo shoe-orange" role="img" aria-label="Navy and orange riptape shoe"></div><span class="name">shoe title</span><span class="type">type</span><span class="price">$ 120</span><a class="add" href="#">Add To Cart <span class="plus">+</span></a></article>
  <article class="card abs" style="left:450px;top:639px"><div class="photo shoe-blue" role="img" aria-label="Navy laced shoe"></div><span class="name">shoe title</span><span class="type">type</span><span class="price">$ 120</span><a class="add" href="#">Add To Cart <span class="plus">+</span></a></article>
  <article class="card abs" style="left:596px;top:639px"><div class="photo shoe-white" role="img" aria-label="Cream leather shoe"></div><span class="name">shoe title</span><span class="type">type</span><span class="price">$ 120</span><a class="add" href="#">Add To Cart <span class="plus">+</span></a></article>
  <article class="card abs" style="left:741px;top:639px"><div class="photo shoe-teal" role="img" aria-label="Teal riptape shoe"></div><span class="name">shoe title</span><span class="type">type</span><span class="price">$ 120</span><a class="add" href="#">Add To Cart <span class="plus">+</span></a></article>

  <article class="card abs" style="left:304px;top:803px"><div class="photo shoe-orange" role="img" aria-label="Navy and orange riptape shoe"></div><span class="name">shoe title</span><span class="type">type</span><span class="price">$ 120</span><a class="add" href="#">Add To Cart <span class="plus">+</span></a></article>
  <article class="card abs" style="left:450px;top:803px"><div class="photo shoe-white" role="img" aria-label="Cream leather shoe"></div><span class="name">shoe title</span><span class="type">type</span><span class="price">$ 120</span><a class="add" href="#">Add To Cart <span class="plus">+</span></a></article>
  <article class="card abs" style="left:596px;top:803px"><div class="photo shoe-blue" role="img" aria-label="Navy laced shoe"></div><span class="name">shoe title</span><span class="type">type</span><span class="price">$ 120</span><a class="add" href="#">Add To Cart <span class="plus">+</span></a></article>
  <article class="card abs" style="left:741px;top:803px"><div class="photo shoe-teal" role="img" aria-label="Teal riptape shoe"></div><span class="name">shoe title</span><span class="type">type</span><span class="price">$ 120</span><a class="add" href="#">Add To Cart <span class="plus">+</span></a></article>
</main>

<footer class="footer abs">
  <div class="col" style="left:114px">
    <h4>WHY SHOP WITH US?</h4>
    <ul><li>Free shipping</li><li>Free return</li><li>14 day right of return</li><li>Large selection</li><li>Accessible Customer Service</li><li>Pay by invoice</li></ul>
  </div>
  <div class="col" style="left:270px">
    <h4>WHAT'S IN STORE?</h4>
    <ul><li>Kids Shoes</li><li>Summer collection</li><li>Shoe</li><li>Footwear brands AZ</li></ul>
  </div>
  <div class="col" style="left:441px">
    <h4>MORE INFORMATION</h4>
    <ul><li>About Us</li><li>Safety</li><li>Terms and conditions</li><li>Shipping Terms</li><li>Become an affiliate</li></ul>
  </div>
  <div class="footer-brand">
    <span class="brand-mark"></span>
    <span class="brand-name">Toddlek</span>
  </div>
  <div class="social"><span aria-label="Social link"></span><span aria-label="Social link"></span><span aria-label="Social link"></span><span aria-label="Email"></span></div>
</footer>
<div class="legal abs">Copyright © Toddlek Shoes Ltd. 2012 All rights reserved</div>

</body>
</html>
```